The Ember Lantern

Look for someone who can add some splash and make this powerpoint presentation more dynamic. Feel free to use color, animations etc to provide some punch.

```html
<!DOCTYPE html>
<html lang="en">
<head>
<meta charset="utf-8">
<title>The Ember Lantern – Deck</title>
<link rel="stylesheet" href="https://fonts.googleapis.com/css2?family=Arimo:wght@700&family=Lato:wght@400;700&display=swap">
<style>
:root{
  --page-bg:#6d6d6d;
  --slide-bg:#ffffff;
  --ink:#1f1f1f;
  --body:#3a3a3a;
  --muted:#9a9a9a;
  --faint:#cfcfcf;
  --rule:#4a4a4a;
  --shape:#e9e9e9;
  --card-shadow:rgba(0,0,0,.10);
}
*{box-sizing:border-box;margin:0;padding:0}
html,body{width:1200px;height:4351px;overflow:hidden}
body{background:var(--page-bg);position:relative;font-family:"Lato",sans-serif;color:var(--body)}
.slide{position:absolute;left:24px;width:1152px;height:648px;background:var(--slide-bg);overflow:hidden}
.slide--cover{top:37px}
.slide--agenda{top:749px}
.slide--about{top:1470px}
.slide--results{top:2192px}
.slide--journey{top:2919px}
.slide--next{top:3639px}
.heading{position:absolute;left:41px;top:62px;font-family:"Arimo",sans-serif;font-weight:700;font-size:30px;color:var(--ink);letter-spacing:.1px}
.footer-url,.footer-page{position:absolute;top:600px;font-size:15px;color:var(--body)}
.footer-url{left:41px}
.footer-page{right:41px}
.footer-brand{position:absolute;left:0;right:0;top:588px;text-align:center;font-size:11px;letter-spacing:3px;color:var(--faint);text-transform:uppercase}
.footer-brand .dot{display:block;width:18px;height:18px;border-radius:50%;border:2px solid var(--faint);margin:0 auto 4px}

/* cover */
.cover-brand{position:absolute;left:0;right:0;top:192px;text-align:center;font-size:23px;letter-spacing:6px;color:var(--faint);text-transform:uppercase}
.cover-brand .dot{display:block;width:42px;height:42px;border-radius:50%;border:3px solid var(--faint);margin:0 auto 18px}
.cover-title{position:absolute;left:0;right:0;top:345px;text-align:center;font-family:"Arimo",sans-serif;font-weight:700;font-size:34px;color:var(--ink);text-transform:uppercase}
.cover-sub{position:absolute;left:0;right:0;top:398px;text-align:center;font-size:21px;color:var(--body)}
.wash{position:absolute;inset:0;background:radial-gradient(ellipse at 70% 40%,#f6f6f6 0%,#ffffff 70%)}

/* agenda */
.agenda-title{position:absolute;left:0;right:0;top:66px;text-align:center;font-family:"Arimo",sans-serif;font-weight:700;font-size:30px;color:var(--ink)}
.agenda-col{position:absolute;top:158px;width:340px;list-style:none}
.agenda-col--left{left:177px}
.agenda-col--right{left:634px}
.agenda-col li{height:64px;padding-top:8px;border-bottom:2px solid var(--rule);font-size:19px;color:var(--body);white-space:nowrap}

/* bullets */
.bullets{position:absolute;list-style:none}
.bullets li{position:relative;padding-left:39px;font-size:16.5px;line-height:27px;color:var(--body)}
.bullets li svg{position:absolute;left:0;top:5px;width:17px;height:17px}

.about-list{left:568px;top:190px;width:490px}
.about-list li{margin-bottom:23px}
.results-list{left:42px;top:155px;width:490px}
.results-list li{margin-bottom:10px}
.next-list{left:133px;top:164px;width:460px}
.next-list li{margin-bottom:16px}

/* media placeholders */
.photo{position:absolute}
.photo--portrait{left:0;top:191px;width:471px;height:457px;background:linear-gradient(135deg,#2a2523 0%,#6e625b 55%,#1d1917 100%)}
.bg-circle{position:absolute;left:829px;top:-118px;width:506px;height:506px;border-radius:50%;background:var(--shape)}
.photo--laptop{left:633px;top:81px;width:440px;height:440px;border-radius:50%;background:linear-gradient(160deg,#a8d4d8 0%,#b79a7a 55%,#6b4f3b 100%)}
.photo--street{left:639px;top:76px;width:513px;height:436px;border-top-left-radius:50px;background:linear-gradient(120deg,#8b2a2a 0%,#c59a4c 40%,#3d4e6e 70%,#a23244 100%)}

/* journey */
.col-title{position:absolute;top:150px;width:463px;text-align:center;font-family:"Arimo",sans-serif;font-weight:700;font-size:21px;color:var(--ink)}
.card{position:absolute;top:203px;width:463px;height:282px;background:#fff;border-radius:10px;box-shadow:0 4px 18px var(--card-shadow)}
.card--then{left:95px}
.card--now{left:600px}
.card .bullets{left:26px;top:40px;width:425px}
.card .bullets li{font-size:16px;line-height:26px;margin-bottom:16px}
</style>
</head>
<body>
<svg width="0" height="0" style="position:absolute" aria-hidden="true">
  <defs>
    <symbol id="arrow-bullet" viewBox="0 0 20 20">
      <circle cx="10" cy="10" r="9" fill="none" stroke="#1f1f1f" stroke-width="2"/>
      <path d="M5 10h7M9 6l4 4-4 4" fill="none" stroke="#1f1f1f" stroke-width="2.4" stroke-linecap="round" stroke-linejoin="round"/>
    </symbol>
  </defs>
</svg>

<!-- Cover -->
<section class="slide slide--cover">
  <div class="wash"></div>
  <div class="cover-brand"><span class="dot"></span>Open Palm Backers</div>
  <h1 class="cover-title">The Ember Lantern</h1>
  <p class="cover-sub">How to raise faster, get back to building and grow</p>
</section>

<!-- Agenda -->
<section class="slide slide--agenda">
  <h2 class="agenda-title">Module One The Fundraising Journey</h2>
  <ul class="agenda-col agenda-col--left">
    <li>Welcome</li>
    <li>About Me &amp; My Background</li>
    <li>Why I created this course</li>
    <li>The Fundraising Journey</li>
    <li>It’s All About The Story</li>
    <li>Accelerators&nbsp; (Good/Bad/Maybe)</li>
  </ul>
  <ul class="agenda-col agenda-col--right">
    <li>Why Not Cedar Ridge Road?</li>
    <li>The different types of capital</li>
    <li>Where to find the&nbsp; accredited investors?</li>
    <li>Unlocking the Power of Angel Investors</li>
    <li>Early-Stage Fundraising Traps</li>
    <li>The Easiest Money You Will Ever Raise</li>
  </ul>
  <span class="footer-url">www.openpalmbackers.com</span>
  <div class="footer-brand"><span class="dot"></span>Open Palm Backers</div>
  <span class="footer-page">Page 02</span>
</section>

<!-- About -->
<section class="slide slide--about">
  <h2 class="heading">About Me &amp; My Background</h2>
  <div class="photo photo--portrait" role="img" aria-label="Portrait photo of the course host, a smiling grey-haired man on a dark background"></div>
  <ul class="bullets about-list">
    <li><svg><use href="#arrow-bullet"/></svg>Over the last 25yrs, I helped two companies build business units to revenues over $1B annually.</li>
    <li><svg><use href="#arrow-bullet"/></svg>Then, in 2018, I burned out.</li>
    <li><svg><use href="#arrow-bullet"/></svg>So, I decided to leave the corporate executive grind to help early-stage founders.</li>
    <li><svg><use href="#arrow-bullet"/></svg>So, I started building my company and brand in 2018.</li>
    <li><svg><use href="#arrow-bullet"/></svg>Since that day, I’ve spent my time finding ways to help early-stage Founders win!</li>
  </ul>
  <div class="footer-brand"><span class="dot"></span>Open Palm Backers</div>
  <span class="footer-page">Page 03</span>
</section>

<!-- Results -->
<section class="slide slide--results">
  <div class="bg-circle"></div>
  <h2 class="heading">Expected Results For Founders</h2>
  <ul class="bullets results-list">
    <li><svg><use href="#arrow-bullet"/></svg>Founders now have a firm understanding of the fundraising process end-to-end</li>
    <li><svg><use href="#arrow-bullet"/></svg>Founder have resources to help them find the right investors at the right time</li>
    <li><svg><use href="#arrow-bullet"/></svg>Founders understand the different types of investors, motivation and stages</li>
    <li><svg><use href="#arrow-bullet"/></svg>Founders understand how to tell their story more effectively</li>
    <li><svg><use href="#arrow-bullet"/></svg>Founders feel equipped to successfully raise capital from the right type of investors</li>
    <li><svg><use href="#arrow-bullet"/></svg>Founders reduce to fundraise from 6-8 months to 3-6 mths</li>
  </ul>
  <div class="photo photo--laptop" role="img" aria-label="Circular photo of hands on a laptop showing a donation page, with a coffee cup and pencil holder on a wooden desk"></div>
  <span class="footer-url">www.openpalmbackers.com</span>
  <div class="footer-brand"><span class="dot"></span>Open Palm Backers</div>
  <span class="footer-page">Page 04</span>
</section>

<!-- Journey -->
<section class="slide slide--journey">
  <h2 class="heading">The Fundraising Journey</h2>
  <h3 class="col-title" style="left:95px">Two Years Ago (2022)</h3>
  <h3 class="col-title" style="left:600px">Today</h3>
  <div class="card card--then">
    <ul class="bullets">
      <li><svg><use href="#arrow-bullet"/></svg>Founders could raise pre-revenue on just a deck</li>
      <li><svg><use href="#arrow-bullet"/></svg>Average number of investor conversations 100-150</li>
      <li><svg><use href="#arrow-bullet"/></svg>Average time to raise 3-6 months</li>
      <li><svg><use href="#arrow-bullet"/></svg>Pre-Seed Valuations $5M-15M</li>
      <li><svg><use href="#arrow-bullet"/></svg>LP’s making decisions in 1-2 calls and FOMO</li>
    </ul>
  </div>
  <div class="card card--now">
    <ul class="bullets">
      <li><svg><use href="#arrow-bullet"/></svg>Founders need customers and revenue ($10K-25K MRR)</li>
      <li><svg><use href="#arrow-bullet"/></svg>Average number of investor conversations 200-300</li>
      <li><svg><use href="#arrow-bullet"/></svg>Average time to raise 5-8 months</li>
      <li><svg><use href="#arrow-bullet"/></svg>Pre-Seed Valuations $3M-10M</li>
      <li><svg><use href="#arrow-bullet"/></svg>LP’s making decision in 4-6 calls</li>
    </ul>
  </div>
  <span class="footer-url">www.openpalmbackers.com</span>
  <div class="footer-brand"><span class="dot"></span>Open Palm Backers</div>
  <span class="footer-page">Page 05</span>
</section>

<!-- Next -->
<section class="slide slide--next">
  <h2 class="heading">What’s Next</h2>
  <ul class="bullets next-list">
    <li><svg><use href="#arrow-bullet"/></svg>Be an entrepreneur and NOT a wantrapreneur</li>
    <li><svg><use href="#arrow-bullet"/></svg>Create your hit list of top 250 investor targets</li>
    <li><svg><use href="#arrow-bullet"/></svg>Control burn</li>
    <li><svg><use href="#arrow-bullet"/></svg>Continue to bootstrap</li>
    <li><svg><use href="#arrow-bullet"/></svg>Pre-Sell product</li>
    <li><svg><use href="#arrow-bullet"/></svg>Continue to grow your network</li>
    <li><svg><use href="#arrow-bullet"/></svg>Attend startup events to practice your pitch</li>
    <li><svg><use href="#arrow-bullet"/></svg>Stop talking and start doing</li>
  </ul>
  <div class="photo photo--street" role="img" aria-label="Photo of two young canvassers with a clipboard and collection jar talking to an older woman at her front door"></div>
  <span class="footer-url">www.openpalmbackers.com</span>
  <div class="footer-brand"><span class="dot"></span>Open Palm Backers</div>
  <span class="footer-page">Page 06</span>
</section>
</body>
</html>
```